Simple, High-Class Web Design Wanted - Motivational Speakers Site

1. Full Brief/Request & Specs outlined on following video -
http://clipvane-recorder.com/watch/tbWrkLmQyP

2. Use colours, images as you feel suits objective (we are happy to pay up to US$30 for any good images but must have licence/permission).

3. Layout probably similar to existing site - www.podiumvoicehub.com.au / http://podiumvoicehub.com.au/contact.php

4. Must Be Able to Coded for MOBILE-FRIENDLINESS & WordPress friendly Ideal.

5. This is the first, small job of many we/graphic design jobs. If suits, winning designer may be offered all future work direct.

Thanks & look forward to your design. Glen.

Target Market(s)

corporates - high end

Number of Pages Required

2 page

Font styles to use
Sans Serif

Requirements
Must have
• Classy professional look
Nice to have
• all in Video in brief
Should not have
• too many images / new images I haven't approved

```html
<!DOCTYPE html>
<html lang="en">
<head>
<meta charset="utf-8">
<title>Podium Voice Hub – Free Guest & Conference Speaker Recommendations</title>
<link href="https://fonts.googleapis.com/css2?family=Open+Sans:wght@400;600;700&family=Roboto+Condensed:wght@400;700&display=swap" rel="stylesheet">
<style>
:root{
  --ink:#111;
  --topbar:#0b0b0b;
  --accent-yellow:#f5d300;
  --headline-blue:#1a7fd8;
  --hero-top:#ffffff;
  --hero-bottom:#dcdcdc;
  --frame:#1c1c1c;
  --cta-dark:#161d28;
  --body-text:#333;
  --panel-blue:#d7e9f5;
  --panel-line:#8fb3cc;
  --alert-red:#d42020;
  --footer-bg:#2b2b2b;
  --footer-text:#cfcfcf;
  --white:#fff;
}
*{box-sizing:border-box;margin:0;padding:0}
html,body{width:733px;height:1200px;overflow:hidden;background:var(--white)}
body{font-family:"Open Sans",Arial,sans-serif;color:var(--body-text);position:relative}
.condensed{font-family:"Roboto Condensed","Arial Narrow",sans-serif}

.topbar{position:absolute;left:0;top:0;width:733px;height:44px;background:var(--topbar);display:flex;align-items:center;justify-content:space-between;padding:0 18px 0 28px;white-space:nowrap}
.topbar__title{font-family:"Roboto Condensed","Arial Narrow",sans-serif;font-weight:700;font-size:21px;color:var(--white);text-transform:uppercase}
.topbar__title em{font-style:normal;color:var(--accent-yellow)}
.topbar__contact{display:flex;align-items:center;gap:10px;color:var(--white);font-family:"Roboto Condensed","Arial Narrow",sans-serif;font-weight:700;font-size:17px}

.hero{position:absolute;left:0;top:44px;width:733px;height:476px;background:linear-gradient(var(--hero-top),var(--hero-bottom))}
.hero__headline{position:absolute;left:30px;right:30px;top:42px;text-align:center;color:var(--headline-blue);font-family:"Roboto Condensed","Arial Narrow",sans-serif;font-size:29px;font-weight:400;line-height:1.2}
.hero__screen{position:absolute;left:171px;top:128px;width:398px;height:258px;background:var(--frame);padding:10px;border-radius:3px}
.hero__photo{width:100%;height:100%;background:radial-gradient(ellipse at 50% 40%,#c9c3bd 0%,#9b9692 55%,#6e6a67 100%)}
.hero__stand{position:absolute;left:266px;top:386px;width:208px;height:14px;background:linear-gradient(#0e0e0e,#3a3a3a);clip-path:polygon(6% 0,94% 0,100% 100%,0 100%)}
.cta{position:absolute;display:flex;align-items:center;justify-content:center;background:var(--cta-dark);color:var(--white);font-family:"Roboto Condensed","Arial Narrow",sans-serif;white-space:nowrap;text-decoration:none}
.cta--event{left:134px;top:456px;width:464px;height:46px;font-size:22px}

.intro{position:absolute;left:44px;right:44px;top:548px;font-size:10.5px;line-height:1.6}
.intro p{margin-bottom:2px}

.criteria{position:absolute;left:120px;top:662px;width:488px;height:170px;background:var(--panel-blue);padding:12px 20px 0 56px;list-style:none}
.criteria li{position:relative;font-size:11px;font-weight:600;color:#222;height:38px;display:flex;align-items:center;white-space:nowrap;border-bottom:1px dashed var(--panel-line)}
.criteria li:last-child{border-bottom:0}
.criteria svg{position:absolute;left:-32px;top:11px}

.closing{position:absolute;left:44px;right:44px;top:850px;font-size:10.5px;line-height:1.6}

.notice{position:absolute;left:54px;top:888px;width:625px;border-bottom:2px solid var(--alert-red);height:24px}
.notice__label{display:inline-block;background:var(--alert-red);color:var(--white);font-weight:700;font-size:12px;padding:4px 10px;height:24px}

.notes{position:absolute;left:56px;right:56px;top:924px;list-style:none;font-size:10px;line-height:1.5}
.notes li{position:relative;padding-left:22px;margin-bottom:9px}
.notes svg{position:absolute;left:0;top:3px}

.cta--contact{left:244px;top:1036px;width:246px;height:40px;font-size:19px;gap:10px}

.footer{position:absolute;left:0;top:1102px;width:733px;height:98px;background:var(--footer-bg);color:var(--footer-text);font-size:10px;text-align:center;padding-top:34px;line-height:1.9}
</style>
</head>
<body>
<header class="topbar">
  <div class="topbar__title"><em>Free Guest</em> &amp; Conference Speaker Recommendations</div>
  <div class="topbar__contact">
    <svg width="22" height="15" viewBox="0 0 22 15" aria-hidden="true"><rect x="1" y="1" width="20" height="13" fill="none" stroke="#fff" stroke-width="2"/><path d="M1 1 L11 9 L21 1" fill="none" stroke="#fff" stroke-width="2"/></svg>
    <svg width="18" height="18" viewBox="0 0 18 18" aria-hidden="true"><path d="M4 1 L7 5 L5 7 C6 10 8 12 11 13 L13 11 L17 14 L15 17 C8 17 1 10 1 3 Z" fill="#fff"/></svg>
    <span>1300 48 21 76</span>
  </div>
</header>

<section class="hero">
  <h1 class="hero__headline">Are you looking for a Guest or Keynote Speaker -<br>Inspiring, Entertaining, Industry Expert etc,</h1>
  <div class="hero__screen"><div class="hero__photo" role="img" aria-label="Video still of a speaker in a light shirt against a grey studio backdrop"></div></div>
  <div class="hero__stand"></div>
  <a class="cta cta--event">I want to Make our Event a Great Success</a>
</section>

<section class="intro">
  <p>Podium Voice Hub is a free industry service designed to help people looking for speakers save precious time and frustration in finding the most suitable/best speaker for their needs.</p>
  <p>Suggestions are given by Australian conference speaker Glen Tarrant, who has presented around Australia for a number of years and is familiar with many of our top professional speakers, MC's as well as the leading speaker bureaus.</p>
  <p>If you would like a hand finding some good speaker options, simply send us the details of your event and the type of presenter you are ideally after, e.g.</p>
</section>

<ul class="criteria">
  <li><svg width="18" height="16" viewBox="0 0 18 16" aria-hidden="true"><path d="M1 8 L6 13 L17 2" fill="none" stroke="#1d2a3a" stroke-width="3"/></svg>Type/Style – Motivational, Entertaining, Keynote/Workshop, MC etc</li>
  <li><svg width="18" height="16" viewBox="0 0 18 16" aria-hidden="true"><path d="M1 8 L6 13 L17 2" fill="none" stroke="#1d2a3a" stroke-width="3"/></svg>Topic/Area - Team Building, Leadership, Inspiration, Health/Life Balance etc</li>
  <li><svg width="18" height="16" viewBox="0 0 18 16" aria-hidden="true"><path d="M1 8 L6 13 L17 2" fill="none" stroke="#1d2a3a" stroke-width="3"/></svg>Approximate Budget - $1000, $2500, $5000, $7500+ etc</li>
  <li><svg width="18" height="16" viewBox="0 0 18 16" aria-hidden="true"><path d="M1 8 L6 13 L17 2" fill="none" stroke="#1d2a3a" stroke-width="3"/></svg>Location - Sydney, Melbourne, Brisbane, Perth, Adelaide, Canberra etc</li>
</ul>

<p class="closing">and where we can, we will be happy to send you some speaker possibilities/ideas, trusted speakers bureaus or simply some thoughts on the best places for you to look. Regards PVH</p>

<div class="notice"><span class="notice__label">Please Note:</span></div>

<ul class="notes">
  <li><svg width="12" height="10" viewBox="0 0 12 10" aria-hidden="true"><path d="M0 5 H9 M6 1 L10 5 L6 9" fill="none" stroke="#444" stroke-width="1.6"/></svg>Any information you provide will ONLY ever be used to help with your specific enquiry</li>
  <li><svg width="12" height="10" viewBox="0 0 12 10" aria-hidden="true"><path d="M0 5 H9 M6 1 L10 5 L6 9" fill="none" stroke="#444" stroke-width="1.6"/></svg>Glen does not have any financial agreements with any individual speakers he recommends. He offers this service, as it only takes a few minutes of his time, helps promote other professional speakers and obviously keeps his own name out there in the industry.</li>
  <li><svg width="12" height="10" viewBox="0 0 12 10" aria-hidden="true"><path d="M0 5 H9 M6 1 L10 5 L6 9" fill="none" stroke="#444" stroke-width="1.6"/></svg>Please understand that while Glen tries to respond quickly, due to his own speaking/travel commitments it may take up to 24 hours.</li>
</ul>

<a class="cta cta--contact">Quick Online Contact Form
  <svg width="16" height="14" viewBox="0 0 16 14" aria-hidden="true"><path d="M0 7 H13 M8 2 L13 7 L8 12" fill="none" stroke="#fff" stroke-width="2.2"/></svg>
</a>

<footer class="footer">
  <p>© 2015. All Rights Reserved www.podiumvoicehub.com.au PO Box 418 Kestrel Bay NSW 2418</p>
  <p>E-mail: hello@podiumvoicehub.com.au Phone: 1300 48 21 76</p>
</footer>
</body>
</html>
```